Cafe Business needs a business card design

I already have an ai logo I would like to use and color. I need someone to make a business card for me on adobe illustrator with it. Its for a cafe restaurant opening in Japan I would like to be able to change out the names, contact info, ect on my own from adobe illustrator.

Industry/Entity Type

Business

Contact Information for Business Card

Double sided with logo on one side and info on the other. Name, Tel, fax, email and west

```html
<!DOCTYPE html>
<html lang="en">
<head>
<meta charset="UTF-8">
<title>Kumo Bean Cafe – Business Card</title>
<link href="https://fonts.googleapis.com/css2?family=Lato:wght@300;400;700;900&display=swap" rel="stylesheet">
<style>
  :root {
    --backdrop: #2e2e2e;
    --espresso: #4a2c17;
    --espresso-light: #6b4327;
    --espresso-deep: #3a2212;
    --cream: #eadcc3;
    --paper: #ffffff;
  }
  * { margin: 0; padding: 0; box-sizing: border-box; }
  html, body {
    width: 1200px;
    height: 800px;
    overflow: hidden;
    background: var(--backdrop);
    font-family: "Lato", Arial, sans-serif;
  }
  .sheet {
    position: relative;
    width: 1200px;
    height: 800px;
    display: flex;
    align-items: center;
    justify-content: center;
    gap: 40px;
  }
  .card {
    position: relative;
    width: 540px;
    height: 310px;
    overflow: hidden;
    box-shadow: 0 10px 24px rgba(0,0,0,0.45);
  }

  /* ---------- Front: contact side ---------- */
  .card--front { background: var(--paper); }
  .card__wave {
    position: absolute;
    inset: 0;
    width: 100%;
    height: 100%;
  }
  .brand {
    position: absolute;
    display: flex;
    align-items: center;
    gap: 12px;
  }
  .brand__square {
    background: var(--espresso);
    flex: none;
  }
  .brand__name {
    font-weight: 900;
    letter-spacing: 0.06em;
    line-height: 1.05;
    text-transform: uppercase;
  }
  .card--front .brand { top: 38px; left: 250px; }
  .card--front .brand__square { width: 58px; height: 58px; }
  .card--front .brand__name { color: var(--espresso); font-size: 19px; }

  .person {
    position: absolute;
    left: 34px;
    bottom: 36px;
    color: var(--paper);
  }
  .person__name {
    font-size: 26px;
    font-weight: 700;
    letter-spacing: 0.02em;
  }
  .person__role {
    font-size: 17px;
    font-weight: 300;
    margin-top: 2px;
  }

  .contact {
    position: absolute;
    left: 268px;
    bottom: 30px;
    list-style: none;
    color: var(--paper);
    font-size: 13.5px;
    font-weight: 400;
    line-height: 1.45;
  }
  .contact__item {
    display: flex;
    align-items: center;
    gap: 7px;
  }
  .contact__icon {
    width: 13px;
    height: 13px;
    flex: none;
  }
  .contact__address { margin-top: 6px; }

  /* ---------- Back: brand side ---------- */
  .card--back {
    background: radial-gradient(ellipse at 45% 40%, var(--espresso-light) 0%, var(--espresso) 45%, var(--espresso-deep) 100%);
  }
  .card--back .brand {
    top: 50%;
    left: 50%;
    transform: translate(-50%, -58%);
    gap: 16px;
  }
  .card--back .brand__square {
    width: 86px;
    height: 86px;
    background: var(--cream);
  }
  .card--back .brand__name { color: var(--cream); font-size: 26px; }
  .website {
    position: absolute;
    right: 30px;
    bottom: 26px;
    color: var(--paper);
    font-size: 13px;
    font-weight: 400;
    letter-spacing: 0.02em;
  }
</style>
</head>
<body>
<main class="sheet">

  <section class="card card--front" aria-label="Business card, contact side">
    <svg class="card__wave" viewBox="0 0 540 310" preserveAspectRatio="none" aria-hidden="true">
      <path d="M0,150 C150,110 360,112 540,158 L540,310 L0,310 Z" fill="var(--cream)"/>
      <path d="M0,162 C150,124 360,126 540,170 L540,310 L0,310 Z" fill="var(--espresso)"/>
    </svg>

    <div class="brand">
      <span class="brand__square"></span>
      <span class="brand__name">Kumo Bean<br>Cafe</span>
    </div>

    <div class="person">
      <p class="person__name">KENJI ARATA</p>
      <p class="person__role">Director</p>
    </div>

    <ul class="contact">
      <li class="contact__item">
        <svg class="contact__icon" viewBox="0 0 16 16" aria-hidden="true"><path fill="#fff" d="M3.6 1.5 5.9 1l1.4 3.4-1.6 1.3a8.5 8.5 0 0 0 4.6 4.6l1.3-1.6 3.4 1.4-.5 2.3c-.2.7-.8 1.1-1.5 1.1C6.6 13.5 2.5 9.4 2.5 3c0-.7.4-1.3 1.1-1.5Z"/></svg>
        555-014-2727
      </li>
      <li class="contact__item">
        <svg class="contact__icon" viewBox="0 0 16 16" aria-hidden="true"><rect x="4" y="1" width="8" height="5" fill="#fff"/><rect x="1.5" y="6.5" width="13" height="8" rx="1" fill="#fff"/></svg>
        555-014-2728
      </li>
      <li class="contact__item">
        <svg class="contact__icon" viewBox="0 0 16 16" aria-hidden="true"><rect x="1" y="3" width="14" height="10" fill="#fff"/><path d="M1.5 3.5 8 9l6.5-5.5M1.5 12.5 6 8m8.5 4.5L10 8" fill="none" stroke="var(--espresso)" stroke-width="1.2"/></svg>
        hello@kumobeancafe.com
      </li>
      <li class="contact__address">1480 Harbor Lane</li>
      <li>Oakridge, California 90210</li>
    </ul>
  </section>

  <section class="card card--back" aria-label="Business card, brand side">
    <div class="brand">
      <span class="brand__square"></span>
      <span class="brand__name">Kumo Bean<br>Cafe</span>
    </div>
    <p class="website">www.kumobeancafe.com</p>
  </section>

</main>
</body>
</html>
```